Zielgruppe
Brokwetter Software
Software Entwicklung
Das Poster soll für interne Zwecke genutzt werden, zB um Bewerbern und neuen Mitarbeitern unsere interne Arbeits- und Teamstruktur zu präsentieren
Aufgabenstellung
Din A2
Querformat
einseitig
Graffiti Style???
bunt, lebendig

```html
<!DOCTYPE html>
<html lang="de">
<head>
<meta charset="utf-8">
<title>Der Sound unseres Teams – Brokwetter Software</title>
<link rel="stylesheet" href="https://fonts.googleapis.com/css2?family=Poppins:wght@500;600;700&display=swap">
<style>
  :root {
    --navy: #1c2a6e;
    --navy-box: #1f3584;
    --white: #ffffff;
    --label-blue: #1f86d0;
    --green-dark: #5fa82c;
    --meter-red: #e2352b;
    --meter-orange: #f28c1f;
    --meter-yellow: #e9e02a;
    --meter-green: #3fae49;
    --tick: #e86b1f;
  }
  * { margin: 0; padding: 0; box-sizing: border-box; }
  html, body { width: 1200px; height: 866px; overflow: hidden; background: #ffffff; }
  .poster {
    position: relative;
    width: 1200px; height: 866px;
    overflow: hidden;
    font-family: 'Poppins', sans-serif;
    color: var(--white);
  }
  .backdrop { position: absolute; inset: 0; }
  .speaker {
    position: absolute; top: 56px; width: 170px; height: 211px;
    background: linear-gradient(160deg, rgba(42,58,150,0.75) 0%, rgba(28,42,110,0.55) 100%);
    border-radius: 6px;
  }
  .speaker--left { left: 63px; }
  .speaker--right { left: 967px; }
  .sound-waves {
    position: absolute; left: 240px; top: 70px; width: 720px; height: 150px;
    background: radial-gradient(ellipse at 50% 55%, rgba(120,200,230,0.28) 0%, rgba(120,200,230,0) 70%);
  }
  .title-words { position: absolute; inset: 0; }
  .header-box {
    position: absolute; top: 287px; height: 43px; width: 249px;
    display: flex; align-items: center; justify-content: center;
    font-weight: 700; border-radius: 6px;
  }
  .header-box--social { left: 63px; background: var(--navy-box); font-size: 23px; }
  .header-box--green {
    background: linear-gradient(180deg, #8fd14f 0%, var(--green-dark) 100%);
    font-size: 19px;
  }
  .tagline {
    position: absolute; left: 63px; top: 340px; width: 249px; height: 23px;
    background: var(--white); color: var(--label-blue);
    font-size: 14px; font-weight: 700; text-align: center; line-height: 23px;
  }
  .meter {
    position: absolute; top: 340px; width: 249px; height: 23px;
    background: #1a2a6a; padding: 3px; border-radius: 2px;
  }
  .meter__scale {
    width: 100%; height: 100%;
    background:
      repeating-linear-gradient(90deg, transparent 0 7px, #1a2a6a 7px 9px),
      linear-gradient(90deg, var(--meter-red) 0%, var(--meter-orange) 28%, var(--meter-yellow) 50%, #9ccc38 66%, var(--meter-green) 100%);
  }
  .meter__marker {
    position: absolute; top: 18px; width: 12px; height: 14px;
    background: var(--tick); border-radius: 50% 50% 50% 50% / 30% 30% 70% 70%;
    border: 1.5px solid #ffffff;
  }
  .task-list { position: absolute; left: 63px; top: 386px; width: 249px; list-style: none; }
  .task {
    height: 30px; margin-bottom: 15px; border-radius: 6px;
    background: var(--navy-box);
    display: flex; align-items: center; justify-content: space-between;
    padding: 0 3px 0 16px;
    font-size: 16px; font-weight: 500; letter-spacing: 0.5px;
  }
  .task__play { width: 29px; height: 29px; }
  .sub-label {
    position: absolute; top: 386px; height: 30px; width: 187px;
    background: var(--white); color: var(--label-blue); border-radius: 6px;
    font-size: 17px; font-weight: 600; text-align: center; line-height: 30px;
  }
  .controls { position: absolute; inset: 0; pointer-events: none; }
  .headline {
    position: absolute; left: 63px; top: 618px;
    font-size: 56px; font-weight: 600; line-height: 54px; letter-spacing: 0.5px;
  }
  .subline {
    position: absolute; left: 63px; top: 734px;
    font-size: 21px; font-weight: 600; color: var(--navy);
  }
  .mascot {
    position: absolute; left: 555px; top: 595px; width: 257px; height: 271px;
    background: radial-gradient(ellipse at 50% 55%, rgba(255,255,255,0.3) 0%, rgba(255,255,255,0) 70%);
  }
  .brand {
    position: absolute; left: 860px; top: 721px; width: 274px; height: 34px;
    background: var(--navy); color: var(--white);
    font-size: 18px; font-weight: 600; letter-spacing: 2px;
    display: flex; align-items: center; justify-content: center;
  }
</style>
</head>
<body>
<main class="poster">
  <svg class="backdrop" width="1200" height="866" viewBox="0 0 1200 866" aria-hidden="true">
    <defs>
      <linearGradient id="sky" x1="0" y1="0" x2="0.2" y2="1">
        <stop offset="0" stop-color="#1a3596"/>
        <stop offset="0.45" stop-color="#1f55bd"/>
        <stop offset="1" stop-color="#2a9ddb"/>
      </linearGradient>
      <radialGradient id="glow" cx="0.5" cy="0.5" r="0.5">
        <stop offset="0" stop-color="#f8d55a" stop-opacity="0.95"/>
        <stop offset="0.45" stop-color="#b9d77a" stop-opacity="0.6"/>
        <stop offset="1" stop-color="#2aa6df" stop-opacity="0"/>
      </radialGradient>
      <radialGradient id="cyanGlow" cx="0.5" cy="0.5" r="0.5">
        <stop offset="0" stop-color="#2fc0e8" stop-opacity="0.8"/>
        <stop offset="1" stop-color="#2fc0e8" stop-opacity="0"/>
      </radialGradient>
    </defs>
    <rect width="1200" height="866" fill="url(#sky)"/>
    <ellipse cx="120" cy="620" rx="320" ry="220" fill="url(#cyanGlow)"/>
    <ellipse cx="580" cy="540" rx="320" ry="200" fill="url(#glow)"/>
    <polygon points="0,694 1200,548 1200,866 0,866" fill="#a8d8f2" fill-opacity="0.45"/>
  </svg>

  <div class="speaker speaker--left" role="img" aria-label="Illustration eines Lautsprechers links"></div>
  <div class="speaker speaker--right" role="img" aria-label="Illustration eines Lautsprechers rechts"></div>
  <div class="sound-waves" role="img" aria-label="Geschwungene Schallwellen zwischen den Lautsprechern"></div>

  <svg class="title-words" width="1200" height="866" viewBox="0 0 1200 866" aria-hidden="true">
    <path id="pathFreiheiten" d="M315 168 Q 440 138 565 188" fill="none"/>
    <path id="pathVertrauen" d="M622 122 Q 750 60 893 100" fill="none"/>
    <text font-family="Poppins, sans-serif" font-weight="700" font-size="34" fill="#ffffff" letter-spacing="1">
      <textPath href="#pathFreiheiten">FREIHEITEN</textPath>
    </text>
    <text font-family="Poppins, sans-serif" font-weight="700" font-size="33" fill="#ffffff" letter-spacing="1">
      <textPath href="#pathVertrauen">VERTRAUEN</textPath>
    </text>
  </svg>

  <div class="header-box header-box--social">SOZIALES</div>
  <div class="header-box header-box--green" style="left:338px">VERANTWORTUNG</div>
  <div class="header-box header-box--green" style="left:613px">SPIELSTÄRKE</div>
  <div class="header-box header-box--green" style="left:889px">INDIVIDUELLER WERT</div>

  <div class="tagline">MEHR GEBEN ALS NEHMEN</div>
  <div class="meter" style="left:338px"><div class="meter__scale"></div><span class="meter__marker" style="left:205px"></span></div>
  <div class="meter" style="left:613px"><div class="meter__scale"></div><span class="meter__marker" style="left:195px"></span></div>
  <div class="meter" style="left:889px"><div class="meter__scale"></div><span class="meter__marker" style="left:224px"></span></div>

  <ul class="task-list">
    <li class="task">MITHELFEN<svg class="task__play" viewBox="0 0 30 30"><circle cx="15" cy="15" r="13" fill="#7cc242" stroke="#d7f0bf" stroke-width="2"/><path d="M12 9 L21 15 L12 21 Z" fill="#1f3584"/></svg></li>
    <li class="task">AUFRÄUMEN<svg class="task__play" viewBox="0 0 30 30"><circle cx="15" cy="15" r="13" fill="#7cc242" stroke="#d7f0bf" stroke-width="2"/><path d="M12 9 L21 15 L12 21 Z" fill="#1f3584"/></svg></li>
    <li class="task">ORGANISIEREN<svg class="task__play" viewBox="0 0 30 30"><circle cx="15" cy="15" r="13" fill="#7cc242" stroke="#d7f0bf" stroke-width="2"/><path d="M12 9 L21 15 L12 21 Z" fill="#1f3584"/></svg></li>
    <li class="task">HÖFLICHKEIT<svg class="task__play" viewBox="0 0 30 30"><circle cx="15" cy="15" r="13" fill="#7cc242" stroke="#d7f0bf" stroke-width="2"/><path d="M12 9 L21 15 L12 21 Z" fill="#1f3584"/></svg></li>
    <li class="task">HYGIENE<svg class="task__play" viewBox="0 0 30 30"><circle cx="15" cy="15" r="13" fill="#7cc242" stroke="#d7f0bf" stroke-width="2"/><path d="M12 9 L21 15 L12 21 Z" fill="#1f3584"/></svg></li>
  </ul>

  <div class="sub-label" style="left:338px">AMBITION</div>
  <div class="sub-label" style="left:540px">ENTHUSIASMUS</div>
  <div class="sub-label" style="left:743px">SCHWÄCHEN</div>
  <div class="sub-label" style="left:946px">STÄRKEN</div>

  <svg class="controls" width="1200" height="866" viewBox="0 0 1200 866" aria-hidden="true">
    <defs>
      <linearGradient id="faderTrack" x1="0" y1="0" x2="0" y2="1">
        <stop offset="0" stop-color="#e2352b"/>
        <stop offset="0.35" stop-color="#f28c1f"/>
        <stop offset="0.7" stop-color="#9ccc38"/>
        <stop offset="1" stop-color="#3fae49"/>
      </linearGradient>
      <g id="faderTicks" stroke="#ffffff" stroke-opacity="0.6" stroke-width="1">
        <line x1="-16" y1="0" x2="-10" y2="0"/><line x1="-16" y1="17" x2="-12" y2="17"/>
        <line x1="-16" y1="34" x2="-12" y2="34"/><line x1="-16" y1="51" x2="-12" y2="51"/>
        <line x1="-16" y1="68" x2="-12" y2="68"/><line x1="-16" y1="85" x2="-10" y2="85"/>
        <line x1="-16" y1="102" x2="-12" y2="102"/><line x1="-16" y1="119" x2="-12" y2="119"/>
        <line x1="-16" y1="136" x2="-12" y2="136"/><line x1="-16" y1="153" x2="-12" y2="153"/>
        <line x1="-16" y1="170" x2="-10" y2="170"/>
      </g>
      <g id="gauge">
        <circle r="27" fill="#1f3584"/>
        <circle r="23" fill="#cfe6fa"/>
        <g fill="none" stroke-width="7">
          <path d="M -16 0 A 16 16 0 0 1 -11.3 -11.3" stroke="#e2352b"/>
          <path d="M -11.3 -11.3 A 16 16 0 0 1 0 -16" stroke="#f28c1f"/>
          <path d="M 0 -16 A 16 16 0 0 1 11.3 -11.3" stroke="#e9e02a"/>
          <path d="M 11.3 -11.3 A 16 16 0 0 1 16 0" stroke="#3fae49"/>
        </g>
        <circle r="8" fill="#1f3584"/>
        <line x1="0" y1="0" x2="-9" y2="-3" stroke="#ffffff" stroke-width="3" stroke-linecap="round"/>
      </g>
    </defs>

    <g class="fader" font-family="Poppins, sans-serif" font-size="10" fill="#c9d6f0">
      <text x="405" y="433" text-anchor="end">MAX</text>
      <text x="405" y="598" text-anchor="end">MIN</text>
      <use href="#faderTicks" x="433" y="427"/>
      <rect x="427" y="425" width="12" height="172" rx="4" fill="url(#faderTrack)" stroke="#1f3584" stroke-width="2"/>
      <rect x="413" y="441" width="40" height="22" rx="3" fill="#ffffff" stroke="#c9d6f0"/>
      <line x1="415" y1="452" x2="451" y2="452" stroke="#9aa7c6" stroke-width="1"/>

      <text x="608" y="433" text-anchor="end">MAX</text>
      <text x="608" y="598" text-anchor="end">MIN</text>
      <use href="#faderTicks" x="636" y="427"/>
      <rect x="630" y="425" width="12" height="172" rx="4" fill="url(#faderTrack)" stroke="#1f3584" stroke-width="2"/>
      <rect x="616" y="458" width="40" height="22" rx="3" fill="#ffffff" stroke="#c9d6f0"/>
      <line x1="618" y1="469" x2="654" y2="469" stroke="#9aa7c6" stroke-width="1"/>
    </g>

    <g class="gauges">
      <use href="#gauge" x="838" y="450"/>
      <use href="#gauge" x="838" y="510"/>
      <use href="#gauge" x="838" y="571"/>
      <use href="#gauge" x="1041" y="450"/>
      <use href="#gauge" x="1041" y="510"/>
      <use href="#gauge" x="1041" y="571"/>
      <use href="#gauge" x="1041" y="632"/>
    </g>
  </svg>

  <h1 class="headline">Der Sound<br>unseres Teams</h1>
  <p class="subline">Teamspirit made by BROKWETTER</p>

  <div class="mascot" role="img" aria-label="Gezeichnete Figur mit erhobenen Armen, die den Teamspirit feiert"></div>

  <div class="brand">BROKWETTER SOFTWARE</div>
</main>
</body>
</html>
```